Night Dresses business cards business requirers

We are a new company initiating Mexico operations. Our core business is Night woman dress (both formal and party dress) for rent. Gownhaven is the name of the company. ITS Gownhaven form by two word. The dress word and topia (Utopic) so the place Gownhaven Means That You cant get the ideal, perfect and unique dress for your event. So we would like a modern, very creative, and attractive business card.

Industry/Entity Type

Womens Clothing

Contact Information for Business Card

Rounded Borders, two faces

Requirements
Must have
• Rounded borders, logo and slogan, modern, glam, attractive design
Should not have
• modern design classic or not

```html
<!DOCTYPE html>
<html lang="en">
<head>
<meta charset="utf-8">
<title>Gownhaven – Business Card</title>
<link href="https://fonts.googleapis.com/css2?family=Open+Sans:wght@400;600;700&display=swap" rel="stylesheet">
<style>
  :root {
    --stage: #ece9e5;
    --card: #ffffff;
    --orchid: #b5508f;
    --slate: #58585b;
    --ink: #555555;
    --white: #ffffff;
  }
  * { margin: 0; padding: 0; box-sizing: border-box; }
  html, body { width: 1200px; height: 987px; overflow: hidden; }
  body {
    background: var(--stage);
    font-family: "Open Sans", Arial, sans-serif;
    position: relative;
  }
  .card {
    position: absolute;
    left: 293px;
    width: 615px;
    height: 351px;
    background: var(--card);
    border-radius: 24px;
    overflow: hidden;
    box-shadow: 0 3px 8px rgba(0,0,0,0.18);
  }
  .card--front { top: 130px; }
  .card--back { top: 505px; }

  .brand {
    position: absolute;
    top: 58px;
    left: 0; right: 0;
    display: flex;
    flex-direction: column;
    align-items: center;
  }
  .brand__name {
    font-size: 28px;
    letter-spacing: 6px;
    color: var(--slate);
    font-weight: 400;
    line-height: 1.2;
  }
  .brand__tagline {
    font-size: 11px;
    letter-spacing: 3px;
    color: var(--slate);
    font-weight: 400;
    margin-top: 4px;
  }

  .person {
    position: absolute;
    top: 156px; left: 0; right: 0;
    text-align: center;
  }
  .person__name { font-size: 21px; font-weight: 600; color: var(--orchid); line-height: 1.2; }
  .person__role { font-size: 16px; color: var(--ink); line-height: 1.3; }

  .band { position: absolute; left: 0; top: 0; width: 615px; height: 351px; }

  .contact {
    position: absolute;
    top: 254px; left: 0; right: 0;
    text-align: center;
    color: var(--white);
    font-size: 15px;
  }
  .contact__address { line-height: 24px; }
  .contact__lines {
    display: flex; justify-content: center; align-items: center;
    gap: 6px; line-height: 28px;
  }
  .contact__item { display: flex; align-items: center; gap: 3px; }
  .contact__item svg { width: 15px; height: 15px; fill: var(--orchid); }
  .contact__web { color: var(--orchid); font-weight: 700; line-height: 24px; }

  .back__name {
    position: absolute;
    top: 128px; left: 0; right: 0;
    text-align: center;
    font-size: 36px;
    letter-spacing: 8px;
    color: var(--orchid);
    font-weight: 600;
  }
  .back__web {
    position: absolute;
    top: 296px; left: 0; right: 0;
    text-align: center;
    font-size: 16px;
    letter-spacing: 7px;
    color: var(--ink);
  }
</style>
</head>
<body>
  <section class="card card--front">
    <svg class="band" viewBox="0 0 615 351" aria-hidden="true">
      <path d="M0 182 Q307 262 615 182 L615 351 L0 351 Z" fill="var(--slate)"/>
      <path d="M0 182 Q307 262 615 182" fill="none" stroke="var(--white)" stroke-width="4"/>
      <path d="M0 176 Q307 256 615 176" fill="none" stroke="var(--orchid)" stroke-width="4"/>
    </svg>

    <div class="brand">
      <span class="brand__name">GOWNHAVEN</span>
      <span class="brand__tagline">EVENING GOWNS TO RENT</span>
    </div>

    <div class="person">
      <p class="person__name">ELENA VARGAS</p>
      <p class="person__role">CEO/Founder</p>
    </div>

    <div class="contact">
      <p class="contact__address">214 Jacaranda Court, Monterrey, NL 64000</p>
      <div class="contact__lines">
        <span class="contact__item">
          <svg viewBox="0 0 16 16"><path d="M3.6 1.5l2.3 2.6-1.2 1.8c.9 2 2.4 3.5 4.4 4.4l1.8-1.2 2.6 2.3-1.3 2.3C6.9 13.5 2.5 9.1 1.3 3.8z"/></svg>555 210 4836
        </span>
        <span class="contact__item">
          <svg viewBox="0 0 16 16"><path d="M4.5 0.5h7a1 1 0 0 1 1 1v13a1 1 0 0 1-1 1h-7a1 1 0 0 1-1-1v-13a1 1 0 0 1 1-1zM5 2.5v10h6v-10zM8 13.2a.7.7 0 1 0 0 1.4.7.7 0 0 0 0-1.4z"/></svg>555 381 7720
        </span>
        <span class="contact__item">
          <svg viewBox="0 0 16 16"><path d="M4 1h8v4H4zM1.5 6h13a1 1 0 0 1 1 1v5h-3v3h-9v-3h-3V7a1 1 0 0 1 1-1zM5 10v3.5h6V10z"/></svg>555 642 0913
        </span>
        <span class="contact__item">
          <svg viewBox="0 0 16 16"><path d="M1 3h14v1.2L8 8.6 1 4.2zM1 5.8l7 4.4 7-4.4V13H1z"/></svg>hello@gownhaven.mx
        </span>
      </div>
      <p class="contact__web">www.gownhaven.mx</p>
    </div>
  </section>

  <section class="card card--back">
    <p class="back__name">GOWNHAVEN</p>
    <p class="back__web">www.gownhaven.mx</p>
  </section>
</body>
</html>
```